Post Card (5x7) - Pre-foreclosure Image - Harbor Path Partners

(Two-Sided Post Card)
FACING FORECLOSURE? YOU STILL HAVE OPTIONS.
If you’re behind on payments or at risk of foreclosure, you’re not alone—and it’s not too late to take action.
We help homeowners:
• Explore options to stay in their home
• Stop or delay foreclosure
• Sell quickly for a fair price if needed
No pressure. No obligation. Just real solutions tailored to your situation.
Call - (240) 558-2094
Email - marcus@hpbllc-mail.com
Harbor Path Partners LLC
7200 Bramwick Lane, Ellicott City, MD 21043
**Marcus Fennimore is a Licensed Realtor with Copperleaf Homes Realty in Bethesda, Maryland.
(Leave room for mailing address, return address & postage)
Target Market(s)
Distressed Homeowners
Industry/Entity Type
Real Estate

```html
<!DOCTYPE html>
<html lang="en">
<head>
<meta charset="utf-8">
<title>Harbor Path Partners – Pre-foreclosure Postcard</title>
<link rel="stylesheet" href="https://fonts.googleapis.com/css2?family=Anton&family=Pathway+Gothic+One&family=Roboto+Condensed:wght@700&family=Rubik:wght@500;600&display=swap">
<style>
  :root {
    --stage: #262626;
    --ink: #000000;
    --paper: #ffffff;
    --gold: #fdbb3e;
    --sunset-top: #f4a84a;
    --sunset-mid: #e9782c;
    --skyline: #3b3b3d;
  }
  * { margin: 0; padding: 0; box-sizing: border-box; }
  html, body { width: 1200px; height: 844px; overflow: hidden; background: var(--stage); }
  .canvas { position: relative; width: 1200px; height: 844px; }

  .card { position: absolute; top: 96px; width: 466px; height: 652px; overflow: hidden; }
  .card--front { left: 128px; background: var(--ink); }
  .card--back { left: 606px; background: var(--paper); }
  .card__shapes { position: absolute; inset: 0; }

  .display { font-family: "Anton", "Impact", sans-serif; text-transform: uppercase; font-weight: 400; }
  .condensed { font-family: "Roboto Condensed", "Arial Narrow", sans-serif; font-weight: 700; }
  .body-sans { font-family: "Rubik", "Helvetica", sans-serif; font-weight: 500; }

  /* front */
  .brand { position: absolute; left: 0; width: 204px; top: 62px; text-align: center; color: var(--paper);
           font-family: "Rubik", sans-serif; font-weight: 500; font-size: 16px; letter-spacing: 3px; line-height: 21px; }
  .headline { position: absolute; left: 24px; top: 222px; font-size: 45px; line-height: 44px; color: var(--ink); }
  .subhead { position: absolute; left: 24px; top: 380px; font-size: 35px; line-height: 42px; color: var(--paper); }
  .rule { position: absolute; height: 6px; background: var(--gold); }
  .rule--front { left: 24px; top: 471px; width: 204px; height: 6px; clip-path: polygon(0 0, 96% 0, 100% 100%, 4% 100%); }
  .lede { position: absolute; left: 24px; top: 526px; font-family: "Pathway Gothic One", "Arial Narrow", sans-serif;
          font-size: 28px; line-height: 28.7px; color: var(--paper); }

  /* back */
  .back-title { position: absolute; left: 22px; top: 26px; font-size: 33px; line-height: 34px; color: var(--ink); }
  .rule--back { left: 0; top: 101px; width: 164px; height: 5px; clip-path: polygon(0 0, 94% 0, 100% 100%, 0 100%); }
  .help-list { position: absolute; left: 21px; top: 118px; list-style: none; font-size: 13.5px; color: var(--ink); }
  .help-list li { position: relative; padding-left: 29px; line-height: 29px; white-space: nowrap; }
  .help-list svg { position: absolute; left: 0; top: 6px; }
  .pill { position: absolute; left: 0; top: 270px; width: 316px; height: 147px; background: var(--ink); border-radius: 0 74px 74px 0; }
  .promise { position: absolute; left: 51px; top: 278px; color: var(--paper); }
  .promise__big { font-size: 32px; line-height: 34px; }
  .promise__small { font-size: 21px; line-height: 26px; margin-top: 5px; }
  .contact-title { position: absolute; left: 20px; top: 436px; font-size: 24px; line-height: 30px; color: var(--ink); }
  .rule--contact { left: 0; top: 467px; width: 108px; height: 5px; clip-path: polygon(0 0, 92% 0, 100% 100%, 0 100%); }
  .contact { position: absolute; left: 22px; top: 486px; color: var(--ink); font-size: 14px; }
  .contact__row { position: relative; padding-left: 25px; white-space: nowrap; }
  .contact__row svg { position: absolute; left: 0; }
  .contact__address { line-height: 16px; }
  .contact__email { margin-top: 7px; line-height: 16px; }
  .contact__phone { margin-top: 4px; font-size: 26px; line-height: 30px; }
  .stamp-box { position: absolute; left: 376px; top: 439px; width: 71px; height: 70px; border: 1px solid #222; }
  .address-line { position: absolute; left: 245px; width: 205px; height: 1px; background: #111; }
  .brand-mark { position: absolute; right: 14px; top: 196px; width: 90px; text-align: center; color: var(--paper);
                font-family: "Rubik", sans-serif; font-weight: 500; font-size: 13px; letter-spacing: 1.5px; line-height: 16px; }
  .footer { position: absolute; left: 0; bottom: 0; width: 466px; height: 42px; background: var(--ink); color: var(--paper);
            font-family: "Rubik", sans-serif; font-weight: 500; font-size: 9.6px; line-height: 42px; text-align: center; white-space: nowrap; }
</style>
</head>
<body>
<main class="canvas">

  <!-- Front -->
  <section class="card card--front">
    <svg class="card__shapes" width="466" height="652" viewBox="0 0 466 652">
      <defs>
        <linearGradient id="sunset-river" x1="0" y1="0" x2="0" y2="1">
          <stop offset="0" stop-color="#8a8c94"/>
          <stop offset="0.3" stop-color="#c98a45"/>
          <stop offset="0.5" stop-color="#f2b451"/>
          <stop offset="0.62" stop-color="#4a3420"/>
          <stop offset="1" stop-color="#2a1a0c"/>
        </linearGradient>
      </defs>
      <path d="M227,442 Q310,572 466,580 L466,533 A265 265 0 0 1 227,442 Z" fill="var(--gold)"/>
      <circle cx="436" cy="270" r="255" fill="url(#sunset-river)" role="img" aria-label="City skyline at sunset reflected on a river"/>
      <circle cx="222" cy="267" r="121" fill="var(--paper)"/>
      <path d="M0,181 H224 A86 86 0 0 1 224,353 H0 Z" fill="var(--gold)"/>
    </svg>

    <div class="brand">HARBOR PATH<br>PARTNERS</div>
    <h1 class="headline display">Facing<br>Foreclosure?</h1>
    <h2 class="subhead display">You still<br>have options.</h2>
    <div class="rule rule--front"></div>
    <p class="lede">If you’re behind on payments<br>or at risk of foreclosure, you’re<br>not alone—and it’s not too late to take action.</p>
  </section>

  <!-- Back -->
  <section class="card card--back">
    <svg class="card__shapes" width="466" height="652" viewBox="0 0 466 652">
      <defs>
        <linearGradient id="skyline-dusk" x1="0" y1="0" x2="0" y2="1">
          <stop offset="0" stop-color="var(--sunset-mid)"/>
          <stop offset="0.25" stop-color="var(--sunset-top)"/>
          <stop offset="0.42" stop-color="var(--skyline)"/>
          <stop offset="1" stop-color="var(--skyline)"/>
        </linearGradient>
      </defs>
      <path d="M243,183 Q320,330 466,358 L466,304 A270 270 0 0 1 243,183 Z" fill="var(--gold)"/>
      <circle cx="470" cy="30" r="262" fill="url(#skyline-dusk)" role="img" aria-label="City skyline silhouette against an orange sunset sky"/>
    </svg>

    <div class="brand-mark">HARBOR<br>PATH<br>PARTNERS</div>

    <h2 class="back-title display">We help<br>homeowners</h2>
    <div class="rule rule--back"></div>
    <ul class="help-list body-sans">
      <li><svg width="17" height="17" viewBox="0 0 17 17"><rect x="1" y="1" width="15" height="15" rx="2" fill="none" stroke="#222" stroke-width="1.6"/><path d="M4.5 8.8l2.6 2.6 5.4-5.6" fill="none" stroke="#222" stroke-width="1.8"/></svg>Explore options to stay<br>in their home</li>
      <li><svg width="17" height="17" viewBox="0 0 17 17"><rect x="1" y="1" width="15" height="15" rx="2" fill="none" stroke="#222" stroke-width="1.6"/><path d="M4.5 8.8l2.6 2.6 5.4-5.6" fill="none" stroke="#222" stroke-width="1.8"/></svg>Stop or delay foreclosure</li>
      <li><svg width="17" height="17" viewBox="0 0 17 17"><rect x="1" y="1" width="15" height="15" rx="2" fill="none" stroke="#222" stroke-width="1.6"/><path d="M4.5 8.8l2.6 2.6 5.4-5.6" fill="none" stroke="#222" stroke-width="1.8"/></svg>Sell quickly for a fair price<br>if needed</li>
    </ul>

    <div class="pill"></div>
    <div class="promise condensed">
      <p class="promise__big">No pressure.<br>No obligation.</p>
      <p class="promise__small">Just real solutions tailored<br>to your situation.</p>
    </div>

    <h3 class="contact-title display">Contact us</h3>
    <div class="rule rule--contact"></div>
    <div class="contact body-sans">
      <p class="contact__row contact__address">
        <svg width="14" height="19" viewBox="0 0 14 19" style="top:2px"><path d="M7 0C3.1 0 0 3 0 6.8 0 11.6 7 19 7 19s7-7.4 7-12.2C14 3 10.9 0 7 0zm0 9.4a2.7 2.7 0 1 1 0-5.4 2.7 2.7 0 0 1 0 5.4z" fill="var(--gold)"/></svg>
        Harbor Path Partners LLC<br>7200 Bramwick Lane,<br>Ellicott City, MD 21043
      </p>
      <p class="contact__row contact__email">
        <svg width="15" height="11" viewBox="0 0 15 11" style="top:3px"><rect width="15" height="11" fill="var(--gold)"/><path d="M0.5 0.8l7 5.4 7-5.4" fill="none" stroke="#fff" stroke-width="1.2"/></svg>
        marcus@hpbllc-mail.com
      </p>
      <p class="contact__row contact__phone condensed">
        <svg width="16" height="16" viewBox="0 0 24 24" style="top:8px"><path d="M6.6 10.8a15.1 15.1 0 0 0 6.6 6.6l2.2-2.2c.3-.3.7-.4 1-.2 1.1.4 2.3.6 3.6.6.6 0 1 .4 1 1V20c0 .6-.4 1-1 1A17 17 0 0 1 3 4c0-.6.4-1 1-1h3.5c.6 0 1 .4 1 1 0 1.3.2 2.5.6 3.6.1.3 0 .7-.2 1z" fill="var(--gold)"/></svg>
        (240) 558-2094
      </p>
    </div>

    <div class="stamp-box"></div>
    <div class="address-line" style="top:531px"></div>
    <div class="address-line" style="top:557px"></div>
    <div class="address-line" style="top:583px"></div>

    <p class="footer">Marcus Fennimore is a Licensed Realtor with Copperleaf Homes Realty in Bethesda, Maryland.</p>
  </section>

</main>
</body>
</html>
```